Delegate Welcome sign

The Copperfield Lodge hotel in Pine Bush NY is welcoming delegations from many different countries during 2019. We want to make a welcome sign about 16:9 ratio about 4 feet high with raised letters. I have attached a background design that we liked and a template with the wording. As you will see I need help with it.

```html
<!DOCTYPE html>
<html lang="en">
<head>
<meta charset="utf-8">
<title>Delegate Welcome Sign – The Copperfield Lodge Hotel</title>
<link href="https://fonts.googleapis.com/css2?family=Open+Sans:wght@400;600;700&display=swap" rel="stylesheet">
<style>
  :root {
    --backdrop: #e8e9e8;
    --board: #1e2926;
    --board-deep: #18211e;
    --leaf-tone: #2b3b36;
    --gold-light: #fbe48a;
    --gold: #e9b82f;
    --gold-deep: #c9921a;
    --silver-light: #ffffff;
    --silver: #d9dcdc;
  }
  html, body {
    margin: 0;
    padding: 0;
    width: 1200px;
    height: 714px;
    overflow: hidden;
    background: var(--backdrop);
    font-family: "Open Sans", sans-serif;
  }
  .welcome-sign {
    position: absolute;
    left: 142px;
    top: 94px;
    width: 910px;
    height: 514px;
    box-shadow: 0 4px 10px rgba(0,0,0,0.25);
    overflow: hidden;
  }
  .sign-background {
    position: absolute;
    inset: 0;
    background: radial-gradient(ellipse at 50% 45%, var(--leaf-tone) 0%, var(--board) 55%, var(--board-deep) 100%);
  }
  .gold-band {
    position: absolute;
    left: 0;
    width: 100%;
    height: 9px;
    background: linear-gradient(180deg, var(--gold-light), var(--gold) 50%, var(--gold-deep));
  }
  .gold-band--top { top: 0; }
  .gold-band--bottom { bottom: 0; }
  .sign-line {
    position: absolute;
    left: 0;
    width: 100%;
    margin: 0;
    text-align: center;
    white-space: nowrap;
  }
  .gold-text {
    background: linear-gradient(180deg, var(--gold-light) 0%, var(--gold) 55%, var(--gold-deep) 100%);
    -webkit-background-clip: text;
    background-clip: text;
    color: transparent;
  }
  .silver-text {
    background: linear-gradient(180deg, var(--silver-light) 0%, var(--silver) 100%);
    -webkit-background-clip: text;
    background-clip: text;
    color: transparent;
    filter: drop-shadow(0 2px 2px rgba(0,0,0,0.6));
  }
  .hotel-name {
    top: 46px;
    font-size: 54px;
    line-height: 60px;
    font-weight: 700;
    filter: drop-shadow(0 2px 3px rgba(0,0,0,0.7));
  }
  .welcomes {
    top: 139px;
    font-size: 40px;
    line-height: 46px;
    font-weight: 400;
    letter-spacing: 1px;
  }
  .welcomes-rule {
    position: absolute;
    top: 161px;
    height: 3px;
    border-radius: 2px;
    background: var(--gold);
  }
  .welcomes-rule--left { left: 122px; width: 190px; }
  .welcomes-rule--right { left: 596px; width: 196px; }
  .event-year {
    top: 198px;
    font-size: 46px;
    line-height: 52px;
    font-weight: 700;
  }
  .delegates {
    top: 257px;
    font-size: 44px;
    line-height: 50px;
    font-weight: 600;
    letter-spacing: 1px;
  }
  .destination {
    font-size: 46px;
    line-height: 52px;
    font-weight: 400;
    letter-spacing: 2px;
  }
  .destination--region { top: 322px; }
  .destination--state { top: 374px; }
  .hashtag {
    top: 445px;
    font-size: 24px;
    line-height: 30px;
    font-weight: 600;
  }
</style>
</head>
<body>
  <section class="welcome-sign">
    <div class="sign-background" role="img" aria-label="Dark green background with a soft pattern of scattered leaves"></div>
    <div class="gold-band gold-band--top"></div>

    <h1 class="sign-line hotel-name gold-text">The Copperfield Lodge Hotel</h1>

    <div class="welcomes-rule welcomes-rule--left"></div>
    <p class="sign-line welcomes gold-text">WELCOMES</p>
    <div class="welcomes-rule welcomes-rule--right"></div>

    <p class="sign-line event-year silver-text">2019</p>
    <p class="sign-line delegates silver-text">International Delegates</p>
    <p class="sign-line destination destination--region silver-text">to the Hudson Valley</p>
    <p class="sign-line destination destination--state silver-text">in New York</p>

    <p class="sign-line hashtag gold-text">#copperfieldlodgehotel</p>

    <div class="gold-band gold-band--bottom"></div>
  </section>
</body>
</html>
```